Popup Nightclub Grand Opening Flyer

We need to design a flyer for the grand opening of an upscale, exclusive nightclub called "Lanternfall". The design needs to be chic and exclusive. The background should be black and the text should primarily be white. We like minimalist designs.

Here is the text for the flyer
-
Velvetrope Atlanta Presents

Lanternfall (LOGO)

A Popup Nightclub Experience
For one night Only

Friday, October 18, 2013
Party begins at 9PM

INVITE ONLY

See invitation for location details
(Velvetrope Atlanta logo)

-
Examples we like

http://cdn2-b.brivelpost.com/sites/default/files/styles/image_content_width/hash/3d/fa/1472093815_4471_flyer.jpg?itok=R8kqWm2z

http://api.plovra.com/files/7Kqq-Tr82XXB3pQzJvmtR5HL2W719E4nbRtC6KLd4HsfM8Y2qTDK-VmjwDoNqLX4QBzTHD9nakRbVx3m-Pfq8htc3MDTWr5p4/2zelSaturdays.jpg

http://quenmar.com/wp-content/uploads/yootheme/widgetkit/gallery/2zel/2zel-gen_vroom4-01.jpg

Hi All, one thing that we are seeing that we don't like is on over emphasis on the phrase "a popup nightclub experience" please don't make this the largest thing on the flyer

Target Market(s)

Target market is 25-35 year olds who are affluent (rich) and like luxury brands

Requirements
Must have
• Dark Background
Nice to have
• Velvetrope Logo on the bottom
Modern text that isn't curvy
Should not have
• Curved text

```html
<!DOCTYPE html>
<html lang="en">
<head>
<meta charset="utf-8">
<title>Lanternfall – A Popup Nightclub Experience</title>
<link rel="stylesheet" href="https://fonts.googleapis.com/css2?family=Cinzel:wght@400;500&family=Montserrat:wght@300;400&family=Roboto+Condensed:wght@700&family=Arimo:wght@700&display=swap">
<style>
  :root {
    --ink: #000000;
    --paper: #ffffff;
    --silver: #d9d9d9;
    --smoke: #2a2a2a;
    --glow: #3a3a3a;
    --mark: #bdbdbd;
  }
  html, body {
    margin: 0;
    padding: 0;
    background: var(--ink);
    overflow: hidden;
  }
  .flyer {
    position: relative;
    width: 927px;
    height: 1200px;
    overflow: hidden;
    background: radial-gradient(ellipse 70% 55% at 50% 62%, var(--glow) 0%, #141414 45%, var(--ink) 80%);
    color: var(--paper);
  }
  .line {
    position: absolute;
    left: 0;
    width: 927px;
    margin: 0;
    text-align: center;
    white-space: nowrap;
  }
  .tagline {
    top: 22px;
    font-family: "Cinzel", serif;
    font-weight: 500;
    font-size: 44px;
    letter-spacing: 2px;
    color: var(--silver);
  }
  .tagline-strong {
    top: 68px;
    font-family: "Cinzel", serif;
    font-weight: 500;
    font-size: 62px;
    letter-spacing: 3px;
    color: var(--silver);
  }
  .glass-art {
    position: absolute;
    left: 195px;
    top: 150px;
    width: 537px;
    height: 890px;
    background: radial-gradient(ellipse 60% 50% at 50% 30%, rgba(90,90,90,0.35) 0%, rgba(40,40,40,0.15) 60%, rgba(0,0,0,0) 100%);
  }
  .presenter {
    top: 196px;
    font-family: "Arimo", sans-serif;
    font-weight: 700;
    font-size: 25px;
    letter-spacing: 0.5px;
  }
  .club-mark {
    position: absolute;
    left: 395px;
    top: 300px;
    width: 136px;
    height: 136px;
    border-radius: 50%;
    background: var(--mark);
  }
  .club-name {
    top: 492px;
    font-family: "Montserrat", sans-serif;
    font-weight: 300;
    font-size: 58px;
    letter-spacing: 10px;
    padding-left: 10px;
    box-sizing: border-box;
  }
  .event-date {
    top: 728px;
    font-family: "Roboto Condensed", sans-serif;
    font-weight: 700;
    font-size: 38px;
    color: var(--silver);
  }
  .event-time {
    top: 775px;
    font-family: "Montserrat", sans-serif;
    font-weight: 400;
    font-size: 20px;
    letter-spacing: 7px;
    padding-left: 7px;
    box-sizing: border-box;
    color: var(--silver);
  }
  .access {
    top: 796px;
    font-family: "Roboto Condensed", sans-serif;
    font-weight: 700;
    font-size: 96px;
    line-height: 1;
    letter-spacing: 1px;
    color: var(--silver);
  }
  .location-note {
    top: 1036px;
    font-family: "Cinzel", serif;
    font-weight: 500;
    font-size: 28px;
    letter-spacing: 1.5px;
    color: var(--silver);
  }
  .host-name {
    top: 1092px;
    font-family: "Montserrat", sans-serif;
    font-weight: 400;
    font-size: 46px;
    letter-spacing: 5px;
    padding-left: 5px;
    box-sizing: border-box;
  }
</style>
</head>
<body>
  <main class="flyer">
    <p class="line tagline">A Popup Nightclub Experience</p>
    <p class="line tagline-strong">FOR ONE NIGHT ONLY</p>

    <div class="glass-art" role="img" aria-label="Large dark martini glass with soft light rays behind it"></div>

    <p class="line presenter">VELVETROPE ATLANTA PRESENTS:</p>

    <div class="club-mark"></div>
    <p class="line club-name">LANTERNFALL</p>

    <p class="line event-date">FRIDAY, OCTOBER 18, 2013</p>
    <p class="line event-time">PARTY BEGINS AT 9PM</p>
    <p class="line access">INVITE ONLY</p>

    <p class="line location-note">See Invitation For Location Details</p>
    <p class="line host-name">VELVETROPE ATLANTA</p>
  </main>
</body>
</html>
```